One Page Website for Personal Trainer in London

I have a logo and need a one page website designed around my branding. I am a freelance Personal Trainer based in London specialising in bodyweight training for men and women. I would like the site to be modern and clean but not overtly urban in design.
I need the following headings:
About Me
My Services
Events
Blog
I don't need them to be seperate pages but if they can link to further down the page that would be great.
Industry/Entity Type
Personal Trainer
Coding
Coded - Design and coding required
Number of Pages Required
1 page
Requirements
Must have
- I need the following headings:
- About Me
- My Services
- Events
- Blog
- mobile friendly formatting
- health and fitness related photography
- Colour scheme in keeping with my existing logo

```html
<!DOCTYPE html>
<html lang="en">
<head>
<meta charset="utf-8">
<title>Marlowe Keane — Personal Training</title>
<link href="https://fonts.googleapis.com/css2?family=Montserrat:wght@500;600&family=Open+Sans:wght@400;600;700&display=swap" rel="stylesheet">
<style>
:root{
  --orange:#f7931e;
  --orange-deep:#f08a12;
  --ink:#222222;
  --text:#444444;
  --muted:#8a8a8a;
  --grey-bg:#efefef;
  --light-bg:#f3f3f3;
  --field:#ececea;
  --footer:#2b2b2b;
  --white:#ffffff;
}
*{box-sizing:border-box;margin:0;padding:0}
html,body{width:1200px;height:4027px;overflow:hidden}
body{position:relative;font-family:"Open Sans",Arial,sans-serif;color:var(--text);background:var(--white)}
.abs{position:absolute}
section,header,footer{position:absolute;left:0;width:1200px}

/* hero */
.hero{top:0;height:805px;background:linear-gradient(135deg,#3b3a38 0%,#6a655e 40%,#4a4642 70%,#2a2826 100%)}
.hero-photo{position:absolute;inset:0;background:radial-gradient(ellipse at 70% 35%,rgba(170,150,130,.45),transparent 55%),linear-gradient(180deg,rgba(0,0,0,.05),rgba(0,0,0,.45))}
.nav{position:absolute;top:46px;left:658px;width:542px;height:30px;background:#111;display:flex;align-items:center;padding-left:26px;font-size:13px;color:#fff}
.nav a{color:#fff;text-decoration:none;padding:0 10px;border-left:1px solid #fff;line-height:12px}
.nav a:first-child{border-left:none;color:var(--orange);padding-left:0}
.brand{position:absolute;left:104px;top:112px;display:flex;align-items:center;gap:10px;font-size:28px;font-weight:600;color:var(--orange)}
.brand-dot{width:22px;height:22px;border-radius:50%;background:var(--orange)}
.hero-kicker{position:absolute;left:0;width:1200px;top:488px;text-align:center;font-family:"Montserrat",sans-serif;font-weight:600;font-size:21px;color:#fff;letter-spacing:.5px}
.hero-title{position:absolute;left:0;width:1200px;top:510px;text-align:center;font-family:"Montserrat",sans-serif;font-weight:500;font-size:80px;line-height:78px;color:var(--orange)}
.dots{position:absolute;top:720px;left:570px;display:flex;gap:12px}
.dots span{width:10px;height:10px;border-radius:50%;background:rgba(255,255,255,.45)}
.dots span:first-child{background:#fff}
.chev{position:absolute}

/* shared */
.sec-title{position:absolute;left:0;width:1200px;text-align:center;font-weight:600;font-size:34px;color:var(--ink)}
.divider{position:absolute;height:2px;background:#555}
.divider i{position:absolute;left:50%;top:-7px;width:16px;height:16px;margin-left:-8px;border-radius:50%;background:var(--orange)}
.to-top{position:absolute;width:42px;height:42px;border-radius:50%;background:var(--orange)}
.to-top svg{position:absolute;left:11px;top:11px}
.photo{position:absolute}

/* about */
.about{top:805px;height:658px;background:var(--white)}
.about-lead{left:118px;top:168px;width:560px;font-size:15px;font-weight:600;color:var(--ink);line-height:18px}
.about-copy{left:118px;top:240px;width:556px;font-size:12.5px;line-height:19px;color:var(--muted)}
.about-copy p{margin-bottom:18px}

/* services */
.services{top:1463px;height:645px;background:var(--grey-bg)}
.card-title{position:absolute;font-size:16px;font-weight:700;color:var(--ink)}
.card-text{position:absolute;width:300px;font-size:12.5px;line-height:19px;color:#555}

/* blog */
.blog{top:2108px;height:612px;background:var(--orange)}
.blog .sec-title{color:#fff}
.blog .divider{background:#fff}
.blog .divider i{background:#fff}
.post-title{position:absolute;width:300px;font-size:18px;font-weight:600;line-height:22px;color:#fff}
.post-date{position:absolute;font-size:12px;color:#fff}
.post-text{position:absolute;width:290px;font-size:12px;line-height:17px;color:#fde0bb}
.post-meta{position:absolute;font-size:12px;color:#fff;display:flex;align-items:center;gap:8px}

/* events & testimonials */
.split{top:2720px;height:408px;background:var(--light-bg)}
.split-title{position:absolute;font-size:28px;font-weight:600;color:var(--orange)}
.split-rule{position:absolute;height:1px;background:#bbb}
.mini-nav{position:absolute;display:flex;gap:6px}
.mini-nav span{width:18px;height:18px;border-radius:50%;background:var(--orange)}
.event-title{position:absolute;left:330px;top:152px;font-size:17px;font-weight:600;color:var(--ink)}
.event-date{position:absolute;left:330px;top:178px;font-size:12px;color:var(--orange)}
.event-text{position:absolute;left:330px;top:198px;width:230px;font-size:12px;line-height:18px;color:#555;text-align:justify}
.avatar{position:absolute;left:660px;top:150px;width:142px;height:142px;border-radius:50%;border:4px solid var(--orange);background:linear-gradient(160deg,#c9b5a4,#8a7364)}
.quote{position:absolute;left:832px;top:148px;width:296px;font-size:12.5px;line-height:19px;color:#555}
.quote b{color:var(--orange);font-size:22px}
.quote-name{position:absolute;left:700px;top:320px;width:62px;text-align:center;font-size:12px;font-weight:600;color:var(--orange)}

/* contact */
.contact{top:3128px;height:577px;background:var(--white)}
.label{position:absolute;font-size:15px;font-weight:600;color:var(--ink)}
.field{position:absolute;background:var(--field);border-radius:20px}
.btn{position:absolute;left:677px;top:422px;width:276px;height:42px;border-radius:21px;background:var(--orange);color:#fff;font-size:16px;font-weight:600;text-align:center;line-height:42px}

/* footer */
.site-footer{top:3705px;height:322px;background:var(--footer);text-align:center}
.addr{position:absolute;left:0;width:1200px;top:66px;font-size:17px;font-weight:700;color:#fff}
.phone{position:absolute;left:0;width:1200px;top:94px;font-size:17px;font-weight:700;color:var(--orange)}
.social{position:absolute;left:548px;top:166px;display:flex;gap:20px}
.social span{width:12px;height:12px;border-radius:50%;background:#fff}
.copy{position:absolute;left:0;width:1200px;top:210px;font-size:11px;color:#888}
</style>
</head>
<body>

<header class="hero">
  <div class="hero-photo" role="img" aria-label="Photo of a woman training with bodyweight exercises in a gym"></div>
  <nav class="nav">
    <a href="#top">Home</a><a href="#about">About Me</a><a href="#services">My Services</a><a href="#events">Events</a><a href="#blog">Blog</a><a href="#contact">Contact us</a>
  </nav>
  <div class="brand"><span class="brand-dot"></span>Marlowe Keane</div>
  <svg class="chev" style="left:58px;top:400px" width="20" height="40" viewBox="0 0 20 40"><path d="M18 2 2 20l16 18" fill="none" stroke="var(--orange)" stroke-width="2"/></svg>
  <svg class="chev" style="left:1122px;top:400px" width="20" height="40" viewBox="0 0 20 40"><path d="M2 2l16 18L2 38" fill="none" stroke="var(--orange)" stroke-width="2"/></svg>
  <p class="hero-kicker">I AM A FREELANCE PERSONAL TRAINER BASED IN LONDON SPECIALISING IN</p>
  <h1 class="hero-title">Bodyweight training<br>for men and women.</h1>
  <div class="dots"><span></span><span></span><span></span><span></span><span></span></div>
</header>

<section class="about" id="about">
  <h2 class="sec-title" style="top:36px">About us</h2>
  <div class="divider" style="left:120px;width:908px;top:108px"><i></i></div>
  <p class="abs about-lead">NEGARE NON POSSUM. DOLORE MALUM EST: IN CRUCEM QUI AGITUR, BEATUS ESSE NON POTEST. QUAE CUM DIXISSET PAULUMQUE INSTITISSET</p>
  <div class="abs about-copy">
    <p>Training should fit your life, not the other way round. I build sessions around simple movements that use nothing more than your own body, so you can train at home, in the park or while travelling. Every plan starts with a proper chat about your goals, your history and the time you really have each week.</p>
    <p>From there we work on strength, mobility and control, adding challenge step by step as you grow more confident.</p>
    <p>I have coached beginners, busy parents, runners and returning athletes across London for over ten years. Sessions are friendly, focused and honest, and you will always know why we are doing each exercise. Whether you want to move without pain, build lean muscle or simply feel fitter, there is a plan that suits you.</p>
  </div>
  <div class="photo" style="left:744px;top:156px;width:335px;height:403px;background:linear-gradient(180deg,#a9b8bf 0%,#c9c3b6 45%,#b59a82 100%)" role="img" aria-label="Photo of the trainer standing on a beach"></div>
  <div class="to-top" style="left:1120px;top:592px"><svg width="20" height="20" viewBox="0 0 20 20"><path d="M10 17V4M4 10l6-6 6 6" fill="none" stroke="#fff" stroke-width="2"/></svg></div>
</section>

<section class="services" id="services">
  <h2 class="sec-title" style="top:66px">Our Service</h2>
  <div class="divider" style="left:120px;width:908px;top:138px"><i></i></div>
  <svg class="chev" style="left:58px;top:290px" width="20" height="40" viewBox="0 0 20 40"><path d="M18 2 2 20l16 18" fill="none" stroke="var(--orange)" stroke-width="2"/></svg>
  <svg class="chev" style="left:1122px;top:290px" width="20" height="40" viewBox="0 0 20 40"><path d="M2 2l16 18L2 38" fill="none" stroke="var(--orange)" stroke-width="2"/></svg>

  <div class="photo" style="left:121px;top:196px;width:303px;height:229px;background:linear-gradient(180deg,#b9cfe0 0%,#dfe7ec 55%,#8e9aa3 100%)" role="img" aria-label="Photo of a woman stretching by the sea"></div>
  <div class="photo" style="left:462px;top:196px;width:301px;height:229px;background:linear-gradient(135deg,#4f88b8 0%,#c89a86 50%,#e9c9a6 100%)" role="img" aria-label="Photo of a woman doing a bodyweight exercise"></div>
  <div class="photo" style="left:800px;top:196px;width:301px;height:229px;background:linear-gradient(135deg,#8f8f8f 0%,#5a6f9e 40%,#d46b4a 75%,#b8b8b8 100%)" role="img" aria-label="Photo of trainers, dumbbells and a fitness plan"></div>

  <h3 class="card-title" style="left:121px;top:450px">Stretching</h3>
  <h3 class="card-title" style="left:462px;top:450px">Bodyweight Excercise</h3>
  <h3 class="card-title" style="left:800px;top:450px">Fitness Plans</h3>
  <p class="card-text" style="left:121px;top:484px">Gentle guided stretching to open tight hips, shoulders and backs. Ideal after long days at a desk, it improves posture, eases stiffness and helps your body recover between harder training sessions.</p>
  <p class="card-text" style="left:462px;top:484px">Push-ups, squats, lunges and holds built into smart circuits. No machines needed, just clear coaching, steady progress and workouts you can repeat anywhere once you know the moves.</p>
  <p class="card-text" style="left:800px;top:484px">A written plan shaped around your goals and schedule, with weekly check-ins, simple food guidance and adjustments as you improve, so you always know exactly what to do next.</p>
  <div class="to-top" style="left:1134px;top:592px"><svg width="20" height="20" viewBox="0 0 20 20"><path d="M10 17V4M4 10l6-6 6 6" fill="none" stroke="#fff" stroke-width="2"/></svg></div>
</section>

<section class="blog" id="blog">
  <h2 class="sec-title" style="top:50px">Latest Blog</h2>
  <div class="divider" style="left:120px;width:908px;top:118px"><i></i></div>

  <div class="photo" style="left:134px;top:161px;width:296px;height:191px;background:linear-gradient(135deg,#5c5750 0%,#b0a396 50%,#e6ddd2 100%)" role="img" aria-label="Photo of a trainer coaching a client in a gym"></div>
  <div class="photo" style="left:470px;top:161px;width:301px;height:191px;background:linear-gradient(135deg,#8fb8c4 0%,#d8b8a4 50%,#5fa7b5 100%)" role="img" aria-label="Photo of a smiling woman lifting light dumbbells"></div>
  <div class="photo" style="left:795px;top:161px;width:295px;height:191px;background:linear-gradient(180deg,#d7e7ef 0%,#b9c9a6 60%,#8a9a7a 100%)" role="img" aria-label="Photo of a couple running outdoors"></div>

  <h3 class="post-title" style="left:134px;top:370px">Alios in primisque familiarem nostrum Posidonium</h3>
  <h3 class="post-title" style="left:470px;top:370px">Utilitatis causa amicitia est quaesita Quicquid</h3>
  <h3 class="post-title" style="left:795px;top:370px">Neque solum ea communia verum etiam paria esse</h3>
  <span class="post-date" style="left:134px;top:416px">November 5, 2017</span>
  <span class="post-date" style="left:470px;top:416px">November 6, 2017</span>
  <span class="post-date" style="left:795px;top:416px">November 7, 2017</span>
  <p class="post-text" style="left:134px;top:440px">Five simple warm-up moves that prepare your joints and muscles for any bodyweight session at home.</p>
  <p class="post-text" style="left:470px;top:440px">Why training with a friend keeps you consistent, and how to plan partner workouts that suit you both.</p>
  <p class="post-text" style="left:795px;top:440px">Running and strength work belong together. Here is a weekly split that balances both without burnout.</p>
  <div class="post-meta" style="left:134px;top:532px"><svg width="16" height="14" viewBox="0 0 16 14"><path d="M8 1C4 1 1 3.4 1 6.3c0 1.6.9 3 2.4 4L2.6 13l3.4-1.8c.6.1 1.3.2 2 .2 4 0 7-2.4 7-5.1S12 1 8 1z" fill="#fff"/></svg>35</div>
  <div class="post-meta" style="left:470px;top:532px"><svg width="16" height="14" viewBox="0 0 16 14"><path d="M8 1C4 1 1 3.4 1 6.3c0 1.6.9 3 2.4 4L2.6 13l3.4-1.8c.6.1 1.3.2 2 .2 4 0 7-2.4 7-5.1S12 1 8 1z" fill="#fff"/></svg>25</div>
  <div class="post-meta" style="left:795px;top:532px"><svg width="16" height="14" viewBox="0 0 16 14"><path d="M8 1C4 1 1 3.4 1 6.3c0 1.6.9 3 2.4 4L2.6 13l3.4-1.8c.6.1 1.3.2 2 .2 4 0 7-2.4 7-5.1S12 1 8 1z" fill="#fff"/></svg>15</div>
  <div class="to-top" style="left:1128px;top:548px;background:#111"><svg width="20" height="20" viewBox="0 0 20 20"><path d="M10 17V4M4 10l6-6 6 6" fill="none" stroke="#fff" stroke-width="2"/></svg></div>
</section>

<section class="split" id="events">
  <h2 class="split-title" style="left:94px;top:70px">Events</h2>
  <div class="mini-nav" style="left:518px;top:82px"><span></span><span></span></div>
  <div class="split-rule" style="left:94px;top:118px;width:470px"></div>
  <div class="photo" style="left:94px;top:150px;width:218px;height:186px;background:linear-gradient(180deg,#b8cbd6 0%,#7c8f6a 55%,#4d5a44 100%)" role="img" aria-label="Photo of a group training outdoors"></div>
  <h3 class="event-title">Verum tamen cum de rebus</h3>
  <span class="event-date">Nov 07, 2017</span>
  <p class="event-text">Join our free outdoor group session in the park this month. Bring water and a mat, and expect a friendly mix of circuits, core work and stretching suitable for every level of fitness. Places are limited, so book early.</p>

  <h2 class="split-title" style="left:663px;top:70px">Testimonials</h2>
  <div class="mini-nav" style="left:1080px;top:82px"><span></span><span></span></div>
  <div class="split-rule" style="left:663px;top:118px;width:445px"></div>
  <div class="avatar" role="img" aria-label="Portrait photo of a client"></div>
  <p class="quote"><b>“</b> Six months ago I could barely manage one push-up. Now I train three times a week, sleep better and feel stronger than ever. The sessions are tough but always fun, and the support is brilliant. <b>”</b></p>
  <span class="quote-name">MARTA</span>
  <div class="to-top" style="left:1128px;top:346px"><svg width="20" height="20" viewBox="0 0 20 20"><path d="M10 17V4M4 10l6-6 6 6" fill="none" stroke="#fff" stroke-width="2"/></svg></div>
</section>

<section class="contact" id="contact">
  <div class="photo" style="left:54px;top:67px;width:443px;height:510px;background:linear-gradient(160deg,#f2f2f2 0%,#c9a58f 40%,#2f2f35 70%,#e05b92 100%)" role="img" aria-label="Photo of a man and woman in workout clothes"></div>
  <h2 class="sec-title" style="left:518px;width:591px;top:86px">Contact us</h2>
  <div class="divider" style="left:518px;width:591px;top:158px"><i></i></div>
  <span class="label" style="left:537px;top:202px">Name</span>
  <span class="label" style="left:840px;top:202px">Email</span>
  <div class="field" style="left:526px;top:228px;width:274px;height:41px"></div>
  <div class="field" style="left:832px;top:228px;width:277px;height:41px"></div>
  <span class="label" style="left:537px;top:278px">Your message</span>
  <div class="field" style="left:526px;top:309px;width:583px;height:75px"></div>
  <div class="btn">Send Message</div>
</section>

<footer class="site-footer">
  <p class="addr">214 Fenwick Road, London E2 7QT</p>
  <p class="phone">Phone (020) 7946 0318</p>
  <div class="social"><span></span><span></span><span></span><span></span></div>
  <p class="copy">© 2017 All rights reserved by Marlowe Keane</p>
</footer>

</body>
</html>
```